Bref créative
Business cards and stationery for investment company
Velorin Holdings
Professional
Owen Pellick
P.O. Box YYY
Brackton, Utah 84219
owen.pellick@velorin.example
www.velorin.example
Logo only

```html
<!DOCTYPE html>
<html lang="en">
<head>
<meta charset="utf-8">
<title>Velorin Holdings – Stationery</title>
<link rel="stylesheet" href="https://fonts.googleapis.com/css2?family=Cinzel:wght@600&family=Open+Sans:wght@400;600&display=swap">
<style>
  :root {
    --backdrop: #5c5c5c;
    --backdrop-light: #787878;
    --brand-red: #d0121b;
    --brand-red-dark: #9e0a10;
    --paper: #ffffff;
    --swoosh-grey: #8a8a8a;
    --ink: #3a3a3a;
    --faint: #ececec;
  }
  * { box-sizing: border-box; margin: 0; padding: 0; }
  html, body { width: 1200px; height: 961px; overflow: hidden; }
  body {
    background: radial-gradient(ellipse at 50% 40%, var(--backdrop-light), var(--backdrop) 75%);
    font-family: "Open Sans", sans-serif;
    position: relative;
  }
  .piece { position: absolute; overflow: hidden; box-shadow: 0 6px 18px rgba(0,0,0,.35); }
  .wordmark {
    font-family: "Cinzel", serif;
    font-weight: 600;
    letter-spacing: .06em;
    text-transform: uppercase;
    white-space: nowrap;
  }
  .tagline { font-family: "Cinzel", serif; font-weight: 600; letter-spacing: .12em; text-transform: uppercase; white-space: nowrap; }

  /* Presentation folder */
  .folder {
    left: 300px; top: 90px; width: 300px; height: 430px;
    background: linear-gradient(160deg, var(--brand-red) 0%, var(--brand-red) 55%, var(--brand-red-dark) 100%);
    color: var(--paper); text-align: center;
  }
  .folder .wordmark { position: absolute; top: 200px; left: 0; right: 0; font-size: 22px; }
  .folder .tagline { position: absolute; top: 234px; left: 0; right: 0; font-size: 9px; }

  /* Letterhead */
  .letterhead { left: 640px; top: 90px; width: 300px; height: 430px; background: var(--paper); }
  .letterhead .wordmark { position: absolute; top: 18px; left: 20px; font-size: 12px; color: var(--brand-red); }
  .letterhead .faint-mark {
    position: absolute; top: 185px; left: 0; right: 0; text-align: center;
    font-size: 26px; color: var(--faint);
  }
  .letterhead svg { position: absolute; left: 0; bottom: 0; }
  .letterhead .contact { position: absolute; right: 20px; bottom: 18px; color: var(--paper); font-size: 6.5px; line-height: 1.6; text-align: left; }

  /* Cup */
  .cup { position: absolute; left: 50px; top: 600px; }

  /* Envelope */
  .envelope { left: 190px; top: 580px; width: 300px; height: 160px; background: var(--paper); }
  .envelope .wordmark { position: absolute; top: 14px; left: 16px; font-size: 11px; color: var(--brand-red); }
  .envelope svg { position: absolute; left: 0; bottom: 0; }

  /* Business card front */
  .card-front { left: 525px; top: 580px; width: 250px; height: 145px; background: var(--paper); }
  .card-front .wordmark { position: absolute; top: 14px; left: 14px; font-size: 11px; color: var(--brand-red); }
  .card-front .contact { position: absolute; top: 40px; left: 14px; font-size: 6.5px; line-height: 1.6; color: var(--ink); }
  .card-front svg { position: absolute; left: 0; bottom: 0; }
  .card-front .person { position: absolute; right: 14px; bottom: 10px; font-size: 8px; font-weight: 600; color: var(--paper); }

  /* Business card back */
  .card-back {
    left: 525px; top: 745px; width: 250px; height: 145px;
    background: linear-gradient(160deg, var(--brand-red), var(--brand-red-dark));
    color: var(--paper); text-align: center;
  }
  .card-back .wordmark { position: absolute; top: 58px; left: 0; right: 0; font-size: 14px; }
  .card-back .tagline { position: absolute; top: 80px; left: 0; right: 0; font-size: 6px; }

  /* Disc */
  .disc { position: absolute; left: 820px; top: 580px; }
</style>
</head>
<body>

  <section class="piece folder" aria-label="Presentation folder">
    <div class="wordmark">Velorin Holdings</div>
    <div class="tagline">Steady Capital Growth</div>
  </section>

  <section class="piece letterhead" aria-label="Letterhead">
    <div class="wordmark">Velorin Holdings</div>
    <div class="faint-mark wordmark">Velorin</div>
    <svg width="300" height="110" viewBox="0 0 300 110" aria-hidden="true">
      <path d="M0 40 C100 70 200 10 300 0 L300 110 L0 110 Z" fill="var(--swoosh-grey)"/>
      <path d="M0 52 C100 80 200 22 300 12 L300 110 L0 110 Z" fill="var(--brand-red)"/>
    </svg>
    <div class="contact">
      Tel 801 555 0142<br>
      P.O. Box YYY, Brackton, Utah 84219<br>
      owen.pellick@velorin.example<br>
      www.velorin.example
    </div>
  </section>

  <svg class="cup" width="110" height="170" viewBox="0 0 110 170" aria-label="Branded cup">
    <rect x="5" y="0" width="100" height="16" rx="5" fill="#f2f2f2"/>
    <path d="M10 16 L100 16 L90 168 L20 168 Z" fill="var(--brand-red)"/>
    <text x="55" y="70" text-anchor="middle" font-family="Cinzel, serif" font-weight="600" font-size="11" fill="#ffffff">VELORIN</text>
  </svg>

  <section class="piece envelope" aria-label="Envelope">
    <div class="wordmark">Velorin Holdings</div>
    <svg width="300" height="80" viewBox="0 0 300 80" aria-hidden="true">
      <path d="M0 30 C110 60 210 10 300 0 L300 80 L0 80 Z" fill="var(--swoosh-grey)"/>
      <path d="M0 42 C110 72 210 22 300 12 L300 80 L0 80 Z" fill="var(--brand-red)"/>
    </svg>
  </section>

  <section class="piece card-front" aria-label="Business card front">
    <div class="wordmark">Velorin Holdings</div>
    <div class="contact">
      Tel 801 555 0142<br>
      P.O. Box YYY, Brackton, Utah 84219<br>
      owen.pellick@velorin.example<br>
      www.velorin.example
    </div>
    <svg width="250" height="45" viewBox="0 0 250 45" aria-hidden="true">
      <path d="M0 10 C90 25 170 0 250 0 L250 45 L0 45 Z" fill="var(--swoosh-grey)"/>
      <path d="M0 18 C90 32 170 8 250 8 L250 45 L0 45 Z" fill="var(--brand-red)"/>
    </svg>
    <div class="person">Owen Pellick</div>
  </section>

  <section class="piece card-back" aria-label="Business card back">
    <div class="wordmark">Velorin Holdings</div>
    <div class="tagline">Steady Capital Growth</div>
  </section>

  <svg class="disc" width="300" height="300" viewBox="0 0 300 300" aria-label="Branded disc">
    <circle cx="150" cy="150" r="145" fill="var(--brand-red)"/>
    <circle cx="150" cy="150" r="40" fill="#c8c8c8"/>
    <circle cx="150" cy="150" r="16" fill="var(--backdrop)"/>
    <text x="150" y="80" text-anchor="middle" font-family="Cinzel, serif" font-weight="600" font-size="16" fill="#ffffff">VELORIN HOLDINGS</text>
  </svg>

</body>
</html>
```